Prescription Savings Card

Looking to revamp our cards that are distributed to pharmacies. Processing information must stand out and be in black with lines through zeros for easy identification.
I have included some previous card designs for consideration. we are looking to go with something cleaner with mainly processing information on the back similar to all white version attached.
Target Market(s)
Pharmacists and Pharmacy Technicians
Industry/Entity Type
prescription medications
Contact Information for Business Card
processing information
Requirements
Must have
- easy to read processing information

```html
<!DOCTYPE html>
<html lang="en">
<head>
<meta charset="utf-8">
<title>Dosewise Prescription Savings Card</title>
<link href="https://fonts.googleapis.com/css2?family=Montserrat:wght@600;700;800&family=Roboto:wght@400;700&display=swap" rel="stylesheet">
<style>
  :root {
    --ink: #000000;
    --red: #ed1c24;
    --orange: #fbb040;
    --navy: #2e3192;
    --royal: #484fdc;
    --cyan: #27aae1;
    --paper: #e6e7e8;
    --panel: #d1d3d4;
    --label: #a7a9ac;
    --white: #ffffff;
  }
  * { box-sizing: border-box; margin: 0; padding: 0; }
  html, body { width: 1200px; height: 1000px; overflow: hidden; }
  body {
    position: relative;
    background: linear-gradient(120deg, #fafafa 0%, #e4e5e6 50%, #c9cacc 100%);
    font-family: "Montserrat", sans-serif;
  }
  .side-label {
    position: absolute;
    font-weight: 800;
    font-size: 31px;
    letter-spacing: 1px;
    color: var(--label);
  }
  .side-label--front { left: 835px; top: 258px; }
  .side-label--back { left: 277px; top: 730px; }

  .card {
    position: absolute;
    width: 630px;
    height: 384px;
    border-radius: 24px;
    overflow: hidden;
    background: var(--ink);
    box-shadow: 6px 10px 14px rgba(0,0,0,0.28);
  }
  .card--front { left: 119px; top: 70px; }
  .card--back { left: 474px; top: 546px; }
  .card__art { position: absolute; inset: 0; width: 630px; height: 384px; }

  .tagline {
    position: absolute;
    font-weight: 700;
    color: var(--ink);
    white-space: nowrap;
    transform-origin: left center;
  }
  .brand-name {
    position: absolute;
    font-weight: 800;
    color: var(--navy);
    letter-spacing: -2px;
    white-space: nowrap;
    line-height: 1;
  }

  .card--front .tagline { left: 57px; top: 108px; font-size: 17px; transform: rotate(-3.6deg); }
  .card--front .brand-name { left: 60px; top: 140px; font-size: 96px; }
  .web-note {
    position: absolute;
    left: 0; right: 0; top: 320px;
    text-align: center;
    font-weight: 700;
    font-size: 12.5px;
    color: var(--white);
    letter-spacing: 0.3px;
  }
  .web-address {
    position: absolute;
    left: 0; right: 0; top: 338px;
    text-align: center;
    font-weight: 700;
    font-size: 22px;
    color: var(--red);
  }

  .benefits { position: absolute; right: 0; top: 0; list-style: none; }
  .benefit {
    position: absolute;
    right: 0;
    height: 25px;
    display: flex;
    align-items: center;
    color: var(--white);
    font-weight: 700;
    font-size: 14.5px;
    border-radius: 6px 0 0 6px;
    white-space: nowrap;
  }
  .benefit::before {
    content: "";
    display: inline-block;
    width: 0; height: 0;
    border-top: 5.5px solid transparent;
    border-bottom: 5.5px solid transparent;
    border-left: 10px solid var(--white);
    margin-right: 14px;
  }
  .benefit--1 { top: 0; width: 377px; padding-left: 20px; background: var(--royal); border-top-right-radius: 24px; }
  .benefit--2 { top: 25px; width: 365px; padding-left: 20px; background: var(--navy); }
  .benefit--3 { top: 50px; width: 357px; padding-left: 20px; background: var(--royal); }
  .benefit--4 { top: 74px; width: 348px; padding-left: 20px; background: var(--navy); }

  .card--back .tagline { left: 26px; top: 148px; font-size: 10px; transform: rotate(-3.6deg); }
  .card--back .brand-name { left: 26px; top: 168px; font-size: 46px; letter-spacing: -1px; }

  .processing { position: absolute; left: 336px; top: 133px; }
  .processing__row {
    display: grid;
    grid-template-columns: 120px 25px auto;
    height: 25.5px;
    align-items: center;
    font-weight: 700;
    font-size: 22px;
    color: var(--ink);
    line-height: 1;
  }
  .processing__row dt, .processing__row dd { display: block; }

  .pharmacy-notice { position: absolute; left: 0; right: 0; top: 316px; color: var(--white); }
  .pharmacy-notice__title {
    text-align: center;
    font-weight: 700;
    font-size: 17px;
    letter-spacing: 0.3px;
  }
  .pharmacy-notice__body {
    margin: 3px 0 0 77px;
    font-family: "Roboto", sans-serif;
    font-size: 12px;
    line-height: 15px;
  }
  .pharmacy-notice__body strong { font-weight: 700; }
</style>
</head>
<body>

  <div class="side-label side-label--front">FRONT</div>
  <div class="side-label side-label--back">BEHIND</div>

  <section class="card card--front" aria-label="Card front">
    <svg class="card__art" viewBox="0 0 1102 673" preserveAspectRatio="none" aria-hidden="true">
      <rect width="1102" height="673" fill="var(--ink)"/>
      <polygon points="0,143 1102,68 1102,76 0,156" fill="var(--orange)"/>
      <polygon points="0,156 1102,76 1102,82 0,191" fill="var(--red)"/>
      <polygon points="0,191 1102,82 1102,440 0,523" fill="var(--paper)"/>
      <polygon points="0,523 1102,440 1102,473 0,537" fill="var(--navy)"/>
      <polygon points="150,528 1102,473 1102,483 0,537" fill="var(--cyan)"/>
    </svg>
    <p class="tagline">PRESCRIPTION AT A DISCOUNT</p>
    <p class="brand-name">Dosewise</p>
    <p class="web-note">CHECK CURRENT PRICING ON OUR WEBSITE</p>
    <p class="web-address">Dosewise.com</p>
  </section>

  <section class="card card--back" aria-label="Card back">
    <svg class="card__art" viewBox="0 0 1102 673" preserveAspectRatio="none" aria-hidden="true">
      <rect width="1102" height="673" fill="var(--ink)"/>
      <polygon points="0,148 520,118 520,126 0,160" fill="var(--orange)"/>
      <polygon points="0,160 520,126 520,140 0,176" fill="var(--red)"/>
      <polygon points="0,176 520,140 520,486 0,521" fill="var(--paper)"/>
      <polygon points="0,521 520,486 520,502 0,535" fill="var(--navy)"/>
      <polygon points="100,530 520,502 520,512 0,536" fill="var(--cyan)"/>
      <polygon points="518,172 1102,172 1102,483 518,512" fill="var(--panel)"/>
    </svg>

    <ul class="benefits">
      <li class="benefit benefit--1">SAVE UP TO 99%</li>
      <li class="benefit benefit--2">100% HIPAA COMPLIANT</li>
      <li class="benefit benefit--3">LOWER PRICE GUARANTEE</li>
      <li class="benefit benefit--4">COVERS 90 DAYS SUPPLY &amp; PET MEDS</li>
    </ul>

    <p class="tagline">PRESCRIPTION AT A DISCOUNT</p>
    <p class="brand-name">Dosewise</p>

    <dl class="processing">
      <div class="processing__row"><dt>BIN</dt><dd>:</dd><dd>014720</dd></div>
      <div class="processing__row"><dt>PCN</dt><dd>:</dd><dd>DSWS2</dd></div>
      <div class="processing__row"><dt>GRP</dt><dd>:</dd><dd>DOSEWISE</dd></div>
      <div class="processing__row"><dt>ID</dt><dd>:</dd><dd>DW0000</dd></div>
      <div class="processing__row"><dt>CONDOR</dt><dd>:</dd><dd>41207</dd></div>
    </dl>

    <div class="pharmacy-notice">
      <p class="pharmacy-notice__title">ATTENTION PHARMACY</p>
      <p class="pharmacy-notice__body">
        If you are unable to process prescription through our program please call <strong>(800) - 555 - 0142</strong><br>
        Administrated by Meridian Claims - This is <strong>NOT INSURANCE</strong>
      </p>
    </div>
  </section>

</body>
</html>
```